A4 Informational Flyer - Summer Pathology Course

We are looking to deliver a QRM57306 Certificate IV in Pathology Summer Course Specifically aimed at current University/TAFE students studying in a health related qualification e.g. Nursing students, Medical students, Pathology students etc.

The basis around it is that our potential students will complete this shortened summer course over the Christmas, new year break 2014/2015 which will enable them to gain further skills in the health related area and they will then be able to work in the pathology field whilst still studying - instead of working a side job at Tollery's to support them.

We would like to use slogans on the flyer for engagement such as "Sick of flipping burgers?" "Are you looking to gain additional skills in a health related field" etc. anything you can come up with as the designer, is also welcomed.

Designer to include information regarding the course as follows:

Course Introduction:

This is a National Training Package and is designed to train people wishing to pursue a career in the Pathology Collection Industry.
The modules within QRM57306 Certificate IV in Pathology provide the participants with training and skills development in a range of areas including Customer Service, Pathology Collection and Techniques, Phlebotomy (blood collection), Infection Control, Occupational Health and Safety and knowledge of the disease processes associated with clients of all ages who may require Pathology Collection.

Government Funding is available for eligible students.

Fees:

Government Funded Student Fees:
Tuition: $425
If you also have a healthcare card, $85
Resources: $355

Fee For Service Student Fees:
Tuition: $2,365
Resources: $355

Method of Study:

The summer QRM57306 Certificate IV in Pathology program is run on campus at both our Kestrel Vale and Ashford Rise training facilities. Students will attend classes two (2) days per week from 9.30am to 2.30pm. Some workbooks are required to be completed off-campus. Extensive practical experience is undertaken in the Verdant Care Academy clinical laboratories.

Course Commencement & Duration:

Course will commence late November 2014 and includes one (1) fast track week and one (1) 4 day week. Classes will conclude by the late January 2015. (Includes 2 week break over Christmas/New Year). *Subject to student numbers

Application Process:

Complete an online enrollment form via our website www.verdantcareacademy.edu.au and our student administration will contact you within 24 hours to discuss your enrollment and the next steps to secure your place on the course.
Alternatively, contact one of our friendly staff members on 03 5172 6408 for further assistance and information.

Please include our attached logos, photos for engagement etc where appropriate.
Please include our website in bold: www.verdantcareacademy.edu.au and our phone number is bold 03 5172 6408

Please also include our "TOID No. 38471" under our logo.

We would like this overall flyer/brochure to be engaging, bold, simply, easy to read for potential students. Keeping with our company colors as much as possible is a must.

Formats must be in a normal format such as PDF for printing purposes and also a JPEG, ESP format so we can use to advertise as a picture on Facebook etc.

Industry/Entity Type

Healthcare

Font styles to use
Serif

Colors
f37123
ffc214
faa54b

Requirements
Must have
• A4, 1 sided please.

Must include codes next to course title.

```html
<!DOCTYPE html>
<html lang="en">
<head>
<meta charset="utf-8">
<title>Verdant Care Academy – Summer Pathology Course</title>
<link rel="stylesheet" href="https://fonts.googleapis.com/css2?family=Roboto+Slab:wght@500;700&family=Tinos:ital,wght@0,400;0,700;1,400;1,700&display=swap">
<style>
  :root {
    --orange: #f37123;
    --yellow: #ffc214;
    --light-orange: #faa54b;
    --red: #e2231a;
    --ink: #1e1e1e;
    --footer: #3a3836;
    --white: #ffffff;
  }
  * { margin: 0; padding: 0; box-sizing: border-box; }
  html, body { width: 848px; height: 1200px; overflow: hidden; background: var(--white); }
  .flyer {
    position: relative; width: 848px; height: 1200px; overflow: hidden;
    font-family: "Tinos", "Times New Roman", serif; color: var(--ink);
  }
  .brand { position: absolute; left: 34px; top: 52px; display: flex; align-items: center; gap: 14px; }
  .brand-dot { width: 44px; height: 44px; border-radius: 50%; background: var(--orange); }
  .brand-name {
    font-family: "Roboto Slab", serif; font-weight: 500; font-size: 31px;
    color: var(--orange); letter-spacing: 0.2px;
  }
  .toid { position: absolute; left: 188px; top: 133px; font-size: 12px; }

  .contact { position: absolute; right: 28px; top: 64px; text-align: right; }
  .contact-row {
    display: flex; justify-content: flex-end; align-items: center; gap: 8px;
    font-weight: 700; font-size: 15px; height: 26px; margin-bottom: 10px;
  }
  .contact-icon {
    width: 25px; height: 25px; border-radius: 50%; background: var(--light-orange);
    display: flex; align-items: center; justify-content: center;
  }

  .rule { position: absolute; left: 0; width: 848px; height: 5px; background: var(--yellow); }
  .rule-top { top: 168px; }
  .rule-bottom { top: 452px; }
  .photo { position: absolute; top: 173px; height: 279px; }
  .photo-anatomy { left: 0; width: 283px; background: linear-gradient(135deg, #e9e4df, #c9b3a4 60%, #b9876f); }
  .photo-collection { left: 285px; width: 281px; background: linear-gradient(135deg, #d8dcdf, #8b8f96 55%, #4a4a55); }
  .photo-tubes { left: 568px; width: 280px; background: linear-gradient(135deg, #a9b6c2, #e6a862 55%, #d9dde2); }

  .headline {
    position: absolute; top: 484px; left: 0; width: 848px; text-align: center;
    font-family: "Tinos", serif; font-weight: 700; font-style: italic;
    font-size: 37px; line-height: 46px; color: var(--red);
  }
  .headline .cta { font-style: normal; }

  .section { position: absolute; left: 33px; width: 782px; }
  .section h2 {
    font-family: "Roboto Slab", serif; font-weight: 700; font-size: 19px; color: var(--ink);
  }
  .section p { font-size: 11.3px; line-height: 15px; margin-top: 12px; text-align: justify; }
  .intro { top: 604px; }
  .funding { top: 736px; }
  .funding h2 { font-size: 20px; }
  .fees { position: absolute; top: 779px; left: 33px; width: 782px; font-size: 12.5px; line-height: 15.5px; }
  .fee-col { position: absolute; top: 0; }
  .fee-col.service { left: 355px; }
  .fee-col h3 { font-weight: 700; font-style: italic; font-size: 12.5px; }
  .method { top: 865px; }
  .commence { top: 975px; }

  .application {
    position: absolute; left: 0; top: 1064px; width: 848px; height: 136px;
    background: var(--footer); padding: 0 33px;
  }
  .dash { position: absolute; left: 0; top: 6px; width: 848px; border-top: 1px dashed var(--light-orange); }
  .application h2 {
    font-family: "Roboto Slab", serif; font-weight: 700; font-size: 20px;
    color: var(--yellow); margin-top: 20px;
  }
  .application p { font-size: 11.3px; line-height: 15.3px; color: var(--light-orange); margin-top: 9px; }
</style>
</head>
<body>
<div class="flyer">
  <header>
    <div class="brand">
      <span class="brand-dot"></span>
      <span class="brand-name">Verdant Care Academy</span>
    </div>
    <div class="toid">TOID No. 38471</div>
    <div class="contact">
      <div class="contact-row">www.verdantcareacademy.edu.au
        <span class="contact-icon"><svg width="13" height="13" viewBox="0 0 14 14"><circle cx="6" cy="6" r="4" fill="none" stroke="#fff" stroke-width="1.8"/><line x1="9" y1="9" x2="13" y2="13" stroke="#fff" stroke-width="2"/></svg></span>
      </div>
      <div class="contact-row">03 5172 6408
        <span class="contact-icon"><svg width="13" height="13" viewBox="0 0 24 24"><path fill="#fff" d="M6.6 10.8a15.1 15.1 0 0 0 6.6 6.6l2.2-2.2c.3-.3.7-.4 1-.2 1.1.4 2.3.6 3.6.6.6 0 1 .4 1 1V20c0 .6-.4 1-1 1A17 17 0 0 1 3 4c0-.6.4-1 1-1h3.5c.6 0 1 .4 1 1 0 1.3.2 2.5.6 3.6.1.3 0 .7-.2 1z"/></svg></span>
      </div>
    </div>
  </header>

  <div class="rule rule-top"></div>
  <div class="photo photo-anatomy" role="img" aria-label="Photo of a tutor pointing at an anatomical torso model"></div>
  <div class="photo photo-collection" role="img" aria-label="Photo of a student collecting blood from a patient's arm while an instructor watches"></div>
  <div class="photo photo-tubes" role="img" aria-label="Photo of a rack of orange-capped blood collection tubes"></div>
  <div class="rule rule-bottom"></div>

  <h1 class="headline">Stop flippin’ and start earning like<br>a health professional. <span class="cta">Enroll Now!</span></h1>

  <section class="section intro">
    <h2>Course Introduction:</h2>
    <p>This is a National Training Package and is designed to train people wishing to pursue a career in the Pathology Collection Industry.<br>The modules within QRM57306 Certificate IV in Pathology provide the participants with training and skills development in a range of areas including Customer Service, Pathology Collection and Techniques, Phlebotomy (blood collection), Infection Control, Occupational Health and Safety and knowledge of the disease processes associated with clients of all ages who may require Pathology Collection?</p>
  </section>

  <section class="section funding">
    <h2>Government Funding is available for eligible students.</h2>
  </section>
  <div class="fees">
    <div class="fee-col funded">
      <h3>Government Funded Student Fees:</h3>
      Tuition: <b>$425</b><br>
      If you also have a healthcare card, <b>$85</b><br>
      Resources: <b>$355</b>
    </div>
    <div class="fee-col service">
      <h3>Fee For Service Student Fees:</h3>
      Tuition: <b>$2,365</b><br>
      Resources: <b>$355</b>
    </div>
  </div>

  <section class="section method">
    <h2>Method of Study:</h2>
    <p>The summer QRM57306 Certificate IV in Pathology program is run on campus at both our Kestrel Vale and Ashford Rise training facilities. Students will attend classes two (2) days per week from 9.30am to 2.30pm. Some workbooks are required to be completed off-campus. Extensive practical experience is undertaken in the Verdant Care Academy clinical laboratories.</p>
  </section>

  <section class="section commence">
    <h2>Course Commencement &amp; Duration:</h2>
    <p>Course will commence late November 2014 and includes one (1) fast track week and one (1) 4 day week. Classes will conclude by the late January 2015. (Includes 2 week break over Christmas/New Year). <b><i>*Subject to student numbers</i></b></p>
  </section>

  <footer class="application">
    <div class="dash"></div>
    <h2>Application Process:</h2>
    <p>Complete an online enrollment form via our website www.verdantcareacademy.edu.au and our student administration will contact you within 24 hours to discuss your enrollment and the next steps to secure your place on the course.<br>
    Alternatively, contact one of our friendly staff members on 03 5172 6408 for further assistance and information.</p>
  </footer>
</div>
</body>
</html>
```